Zentrova - Creative Automation

We are a software house for Audio Visual Systems integration/automation and home automation. we develop innovative software to automate a variety of devices mainly related to audio visuals and we design touch panel user interfaces to control these systems.

We would like to see designs that stick to our colours and theme, which you can find on our webpage www.zentrova.com.au

The final design should communicate touch panels, innovation, software and automation.

Industry/Entity Type

Software

Requirements
Must have
• The business card must show the following information:
Name example : Derek Malloway
Qualification example: B Eng ICT(CompSys) Dip EngPrac
Title example : Control Systems Programmer
Mobile Phone, Company phone, Email address ,Company website

```html
<!DOCTYPE html>
<html lang="en">
<head>
<meta charset="utf-8">
<title>Zentrova - Creative Automation business card</title>
<link href="https://fonts.googleapis.com/css2?family=Mulish:wght@400;700&display=swap" rel="stylesheet">
<style>
  :root {
    --backdrop: #2b2b2b;
    --card: #ffffff;
    --brand-blue: #2074c2;
    --brand-green: #1a9b5a;
    --ink: #3a3a3a;
    --muted: #6a6a6a;
    --rule: #c8c8c8;
  }
  * { margin: 0; padding: 0; box-sizing: border-box; }
  html, body { width: 1200px; height: 750px; overflow: hidden; }
  body {
    position: relative;
    background: var(--backdrop);
    font-family: "Mulish", Arial, sans-serif;
    color: var(--ink);
  }
  .card {
    position: absolute;
    width: 511px;
    height: 292px;
    background: var(--card);
    border-radius: 10px;
    overflow: hidden;
  }
  .card-front { left: 77px; top: 118px; }
  .card-back { left: 613px; top: 325px; }

  .brand {
    position: absolute;
    display: flex;
    align-items: center;
    gap: 8px;
  }
  .brand-square {
    width: 38px; height: 38px;
    background: var(--brand-blue);
    border-radius: 4px;
  }
  .brand-name {
    font-weight: 700;
    font-size: 26px;
    color: var(--brand-green);
    letter-spacing: 0.2px;
  }
  .card-front .brand { left: 19px; top: 22px; }
  .card-back .brand { left: 129px; top: 126px; }
  .card-back .brand-square { width: 50px; height: 50px; }
  .card-back .brand-name { font-size: 32px; }

  .person { position: absolute; left: 243px; top: 106px; }
  .person-name {
    font-weight: 700;
    font-size: 20px;
    color: var(--brand-blue);
    line-height: 1.1;
  }
  .person-qualification {
    font-size: 10.5px;
    color: var(--muted);
    margin-top: 3px;
    line-height: 1.2;
  }
  .person-title { font-size: 12px; margin-top: 2px; line-height: 1.2; }

  .divider {
    position: absolute;
    left: 229px; top: 174px;
    width: 1px; height: 84px;
    background: var(--rule);
  }
  .address {
    position: absolute;
    right: 298px; top: 218px;
    text-align: right;
    font-size: 12px;
    line-height: 16px;
    font-style: normal;
  }
  .contacts {
    position: absolute;
    left: 244px; top: 185px;
    list-style: none;
    font-size: 12.5px;
  }
  .contacts li {
    display: flex;
    align-items: center;
    gap: 7px;
    height: 16.5px;
  }
  .contacts svg { width: 11px; height: 11px; flex: none; }

  .band { position: absolute; left: 0; bottom: 0; width: 511px; height: 20px; }

  .site {
    position: absolute;
    left: 0; right: 0; top: 266px;
    text-align: center;
    font-size: 13px;
  }
</style>
</head>
<body>

<section class="card card-front" aria-label="Business card front">
  <div class="brand">
    <span class="brand-square"></span>
    <span class="brand-name">zentrova</span>
  </div>

  <div class="person">
    <h1 class="person-name">Derek Malloway</h1>
    <p class="person-title">Control Systems Programmer</p>
    <p class="person-qualification">B Eng ICT(CompSys) Dip EngPrac</p>
  </div>

  <address class="address">12 Millbrook Lane<br>Harlow Vale, NSW, 2790</address>
  <div class="divider"></div>

  <ul class="contacts">
    <li>
      <svg viewBox="0 0 12 12"><rect x="3" y="0.5" width="6" height="11" rx="1.5" fill="var(--brand-blue)"/><rect x="4" y="2" width="4" height="6" fill="#fff"/></svg>
      0400 555 218
    </li>
    <li>
      <svg viewBox="0 0 12 12"><circle cx="6" cy="6" r="6" fill="var(--brand-blue)"/><path d="M4 3 L5.5 3 L6 5 L5 5.6 Q5.8 7 6.6 7.2 L7.2 6.3 L9 7 L9 8.5 Q5 9 3.5 4 Z" fill="#fff"/></svg>
      0255 010 384
    </li>
    <li>
      <svg viewBox="0 0 12 12"><rect x="0.5" y="2" width="11" height="8" rx="2" fill="var(--brand-blue)"/><rect x="2.5" y="4" width="7" height="4" fill="#fff"/></svg>
      dmalloway@zentrova.com.au
    </li>
    <li>
      <svg viewBox="0 0 12 12"><circle cx="6" cy="6" r="5.5" fill="var(--brand-blue)"/><path d="M1 6 H11 M6 1 V11 M3 3 Q6 5 9 3 M3 9 Q6 7 9 9" stroke="#fff" stroke-width="0.8" fill="none"/></svg>
      www.zentrova.com.au
    </li>
  </ul>

  <svg class="band" viewBox="0 0 511 20" preserveAspectRatio="none" aria-hidden="true">
    <polygon points="0,0 346,0 356,20 0,20" fill="var(--brand-green)"/>
    <polygon points="350,6 511,6 511,20 357,20" fill="var(--brand-blue)"/>
  </svg>
</section>

<section class="card card-back" aria-label="Business card back">
  <div class="brand">
    <span class="brand-square"></span>
    <span class="brand-name">zentrova</span>
  </div>
  <p class="site">www.zentrova.com.au</p>
</section>

</body>
</html>
```